In need of a Wordpress website for a Water Sports Rental Company!

We are starting a new venture that provides a variety of rental equipment in the Cayman Islands. We are in need of a website where guests are able to book their rental gear during their stay in Cayman. We will also have an interactive map where guests can learn about off the beaten path activities to explore in here Cayman.

Our target market is middle/upper class, so we need a website that appeals to this group. We need our website to be clean, simple and easy to navigate. We need it to be highly visual and modern. We like the idea of the website having a tropical feel to it, we are very open to creative ideas that reflects this!

Must be designed in WordPress using the Quelmira template I’ve provided.

You will find all instructions & the photos I want to use for this website on the following vaultra account:
- www.vaultra.com
- Username: fun@marlettoboats.com
- Password: lantern4

All of the photos will need to be resized accordingly to be as small as possible without loosing resolution.

These are the tabs that will be used:
- Home Page
- Adventure Map
- Rental Gear
- Tours
- Photo Gallery
- Contact Us

Home Page
- You will find all the text and instructions for the home page in the word document named ‘Home Page’.

Adventure Map
- You will find all the text and instructions for the home page in the word document named ‘Adventure Map Content’
- There will also be a few 'guide' pages under this tab, which we will go in to detail with the winner.

Rentals
- You will find all the text and instructions for the Rentals page in the word document named ‘Rentals Content’

Tours
- This will just be a page saying ‘kayaking, snorkeling & Bioluminescence tours coming soon’.

Photo Gallery
- You will find the photos for this in our Vaultra.com Account

Contact Us
- Send us a Message – page will be similar to our other site http://marlettoboats.com/contact/
- Phone: +1 (345) 555 0182
- Email: fun@zolvatrek.com

The big factors on who will have the winning design are:
- The background used
- The layout of the Home Page
- The animations at the top of the Rental Landing Page
- The overall clean, professional look to the website

If you have any questions, don't hesitate to ask.

We look forward to working with you all!!

Good luck!!

Target Market(s)

Middle/Upper Class on vacation with their family

Industry/Entity Type

It Company

Coding

Coded - Design and coding required

Number of Pages Required

5+ page

Colors
fffbf0
cadf82
fbf289
f6faec
fdf9cf
eaf2ce
fff3d1
fee18a
abd037

Requirements
Must have
• - Must be designed in Wordpress using the Quelmira template I have provided or another suitable web template.
• - Must be Responsive Web Design so that the website adjusts to various screen sizes.

```html
<!DOCTYPE html>
<html lang="en">
<head>
<meta charset="utf-8">
<title>Tidewake Rentals – Cayman's Premier Adventure and Rental Company</title>
<link href="https://fonts.googleapis.com/css2?family=Open+Sans:wght@400;600;700;800&family=Courgette&display=swap" rel="stylesheet">
<style>
:root{
  --page:#f3f4f2;
  --paper:#ffffff;
  --ink:#333333;
  --muted:#555555;
  --lime:#abd037;
  --lime-soft:#cadf82;
  --navbar:#d9dad6;
  --footer:#0f4a73;
  --footer-deep:#0a3456;
  --bottombar:#e6e7e4;
  --sky:#5fa8e0;
  --cloud:#e6f1f7;
  --sand:#e6d9bb;
  --aqua:#45c2c4;
  --teal:#2a98a8;
  --deep:#1c5f93;
}
*{box-sizing:border-box;margin:0;padding:0}
html,body{width:1200px;height:3543px;overflow:hidden}
body{position:relative;background:var(--page);font-family:"Open Sans",Arial,sans-serif;color:var(--ink)}
.abs{position:absolute}

/* header */
.site-header{left:0;top:0;width:1200px;height:194px;background:linear-gradient(#fafafa,#eeeeec)}
.brand{left:0;width:1200px;top:22px;display:flex;justify-content:center;align-items:center;gap:14px}
.brand-mark{width:60px;height:60px;border-radius:50%;background:var(--lime)}
.brand-name{font-weight:800;font-size:32px;color:#1e2a1c;letter-spacing:1px}
.tagline{left:0;width:1200px;top:122px;text-align:center;font-family:"Courgette",cursive;font-size:24px;color:var(--lime)}
.header-wave{left:0;top:160px}
.main-nav{left:0;top:194px;width:1200px;height:35px;background:var(--navbar);display:flex;justify-content:center;align-items:center;gap:40px}
.main-nav a{font-weight:700;font-size:14px;color:#222;text-decoration:none;text-transform:uppercase}

/* hero */
.hero{left:0;top:229px;width:1200px;height:420px;
  background:
    radial-gradient(ellipse 320px 260px at 300px 200px,rgba(255,230,120,.45),rgba(255,230,120,0) 70%),
    radial-gradient(ellipse 360px 280px at 640px 240px,rgba(214,232,70,.55),rgba(214,232,70,0) 70%),
    radial-gradient(ellipse 900px 140px at 600px 0,rgba(255,255,255,.7),rgba(255,255,255,0) 80%),
    linear-gradient(175deg,#a8e3ee 0%,#55bfd8 35%,#2f9ec8 65%,#1f77ac 100%)}
.hero-wave{left:0;top:540px}

/* features */
.feature{top:685px;height:347px;background:var(--paper);box-shadow:0 2px 6px rgba(0,0,0,.12)}
.feature .photo{position:absolute;left:10px;right:10px;top:8px;height:158px}
.feature h3{position:absolute;left:20px;top:182px;font-size:19px;font-weight:600;color:#222}
.feature p{position:absolute;left:20px;right:18px;top:220px;font-size:13px;line-height:21px;color:var(--muted)}

/* welcome */
.welcome-title{left:0;width:1200px;top:1090px;text-align:center;font-family:"Courgette",cursive;font-weight:400;font-size:29px;color:#222}
.welcome-title span{color:var(--lime)}
.welcome-text{left:125px;width:950px;top:1144px;text-align:center;font-size:14.5px;line-height:23px;color:var(--muted)}

/* ocean band */
.ocean{left:0;top:1299px;width:1200px;height:1323px;
  background:
    radial-gradient(ellipse 500px 300px at 150px 150px,rgba(110,90,200,.45),rgba(110,90,200,0) 70%),
    radial-gradient(ellipse 600px 400px at 1050px 250px,rgba(90,120,210,.4),rgba(90,120,210,0) 70%),
    linear-gradient(180deg,#3f78c0 0%,#2f9ebf 38%,#3cbab6 70%,#2a8fb0 100%)}
.tile-photo{position:absolute}
.tile-card{position:absolute;background:var(--paper);padding:22px 22px 0 22px;overflow:hidden}
.tile-card h4{font-size:13px;font-weight:700;text-transform:uppercase;line-height:19px;color:#222;margin-bottom:8px}
.tile-card p{font-size:12px;line-height:18.5px;color:var(--muted)}

/* top picks */
.picks-title{left:0;width:1200px;top:2676px;text-align:center;font-size:23px;font-weight:700;letter-spacing:1px;color:#333;text-transform:uppercase}
.pick{top:2735px;width:246px}
.pick .shape{display:block}
.pick h5{margin-top:20px;font-size:13.5px;font-weight:700;text-transform:uppercase;color:#222}
.pick p{margin-top:8px;font-size:12.5px;line-height:18px;color:var(--muted);width:230px}
.read-more{display:inline-block;margin-top:30px;width:111px;height:30px;line-height:30px;text-align:center;background:var(--lime);color:#fff;font-size:12px;font-weight:600;text-decoration:none}

/* footer */
.site-footer{left:0;top:3130px;width:1200px;height:361px;
  background:
    radial-gradient(ellipse 500px 220px at 600px 180px,rgba(60,120,110,.45),rgba(60,120,110,0) 70%),
    linear-gradient(180deg,var(--footer) 0%,#16628f 45%,var(--footer-deep) 100%)}
.footer-col{top:3190px;list-style:none}
.footer-col li{font-size:15.5px;line-height:31.5px;color:#fff}
.footer-contact{left:652px;top:3190px;color:#fff;font-size:15px;line-height:24px}
.footer-contact .gap{height:22px}
.footer-address{line-height:20px;font-size:14px}
.partner-badge{left:945px;top:3224px;width:137px;height:142px;background:#fff;border:8px solid #7cc576}
.bottom-bar{left:0;top:3491px;width:1200px;height:52px;background:var(--bottombar);text-align:center;line-height:52px;font-size:14px;color:#888}
</style>
</head>
<body>

<header class="site-header abs"></header>
<div class="brand abs"><span class="brand-mark"></span><span class="brand-name">Tidewake Rentals</span></div>
<div class="tagline abs">Cayman's Premier Adventure and Rental Company</div>
<svg class="header-wave abs" width="1200" height="30" viewBox="0 0 1200 30" aria-hidden="true">
  <path d="M0 22 C200 4 380 30 600 14 S1000 2 1200 18" fill="none" stroke="var(--lime)" stroke-width="4"/>
</svg>
<nav class="main-nav abs">
  <a href="#">Rental Gear</a><a href="#">Adventure Map</a><a href="#">Tours</a><a href="#">Photo Gallery</a><a href="#">Contact Us</a>
</nav>

<div class="hero abs" role="img" aria-label="Two snorkelers underwater in clear turquoise sea among tropical fish"></div>
<svg class="hero-wave abs" width="1200" height="110" viewBox="0 0 1200 110" aria-hidden="true">
  <path d="M0 50 C250 110 500 20 760 60 S1080 90 1200 40 L1200 110 L0 110 Z" fill="var(--page)"/>
</svg>

<section>
  <article class="feature abs" style="left:118px;width:314px">
    <div class="photo" role="img" aria-label="Two people paddling a blue kayak on calm water" style="background:linear-gradient(180deg,#8fc4e6 0%,#cfe6ee 30%,#5cc1c9 55%,#2f9fb4 80%,#2d5fb0 100%)"></div>
    <h3>Exploration</h3>
    <p>Rent everything you need to get outside and explore the island on your own terms. Snorkel the Kittiwake, check out the bioluminescence and much more with your own gear!</p>
  </article>
  <article class="feature abs" style="left:444px;width:307px">
    <div class="photo" role="img" aria-label="Person relaxing on a blue inflatable kayak in turquoise water" style="background:linear-gradient(180deg,#7fd3d6 0%,#4fbfc6 45%,#2c6fbf 62%,#38a9b8 78%,#2a9bb0 100%)"></div>
    <h3>Relaxation</h3>
    <p>We will come straight to your resort or condo and set everything up for you and your family to enjoy our kayaks and paddle boards on the beautiful calm waters off Seven Mile Beach.</p>
  </article>
  <article class="feature abs" style="left:763px;width:317px">
    <div class="photo" role="img" aria-label="Two snorkelers in full face masks underwater" style="background:linear-gradient(120deg,#4fb4d6 0%,#d9789e 30%,#3a8fc8 55%,#1f6fa6 100%)"></div>
    <h3>Education</h3>
    <p>We love sharing our knowledge on Cayman's history and the island's extraordinary marine life. We'll also teach you everything you need to find those secluded spots on your adventures.</p>
  </article>
</section>

<h2 class="welcome-title abs">Welcome to <span>Tidewake Rentals!</span></h2>
<p class="welcome-text abs">We love having the freedom to explore when travelling and we bet you do too! We are Grand Cayman's premier rental company, offering everything you need to make the most of your vacation. Our website serves as a great starting point to help you prepare for your vacation here in Cayman. We feature a huge selection of adventures on our interactive map with tons of useful information, pictures and directions. Our adventure map is the perfect guide to all our great spots to check out here in Cayman.</p>

<section class="ocean abs" role="img" aria-label="Clear blue and turquoise sea water seen from above"></section>

<!-- column one -->
<div class="tile-photo" role="img" aria-label="Two kids jumping on a beach under a blue sky" style="left:118px;top:1358px;width:319px;height:189px;background:linear-gradient(180deg,#3f8fd6 0%,#7fb8e6 30%,#eef4f7 55%,#cfe2ea 72%,#e8dcc0 86%,#d9c9a4 100%)"></div>
<div class="tile-card" style="left:118px;top:1547px;width:319px;height:224px">
  <h4>Your one stop shop for all the rentals you need here in Cayman!</h4>
  <p>We have a have a huge array of fun toys and equipment for you to enjoy. Whether it's for exploring or relaxing, we have all the equipment you need to make the most of your trip here in Cayman. Need something that we don't stock, just ask and we'll do everything we can to get you the gear you need!</p>
</div>
<div class="tile-photo" role="img" aria-label="Kayaks and a small sailboat on shallow turquoise water" style="left:118px;top:1776px;width:319px;height:574px;background:linear-gradient(180deg,#3aa9b3 0%,#6fd0c6 22%,#48c1bd 45%,#2fa7b0 70%,#2b98a8 100%)"></div>
<div class="tile-card" style="left:118px;top:2350px;width:319px;height:232px">
  <h4>Your one stop shop for all the rentals you need here in Cayman!</h4>
  <p>When we come to deliver your equipment, we teach you everything you need to know about the island including the best hidden spots, best restaurants &amp; bars to eat &amp; drink and anything else you might be curious about. Please don't hesitate to contact us for any and all of your vacation questions. We are happy to help!</p>
</div>

<!-- column two -->
<div class="tile-photo" role="img" aria-label="Three children standing on a paddle board with arms raised" style="left:442px;top:1358px;width:318px;height:418px;background:linear-gradient(180deg,#4f9fdf 0%,#9cc8ea 25%,#e6f0f4 50%,#a9d3dc 68%,#4fb6c4 85%,#3aa6b8 100%)"></div>
<div class="tile-card" style="left:442px;top:1776px;width:318px;height:196px">
  <h4>Your one stop shop for all the rentals you need here in Cayman!</h4>
  <p>You won't find any tourist traps on our map! We're all about getting off the beaten path and finding those unique spots and natural wonders to explore. Get our expert advice on which adventures are best for you and how to tackle them!</p>
</div>
<div class="tile-photo" role="img" aria-label="Stingrays gliding over a sandy sea floor" style="left:442px;top:1979px;width:318px;height:277px;background:linear-gradient(160deg,#7cc3c4 0%,#5aa9b0 40%,#8a9a8c 60%,#3e8f9c 100%)"></div>
<div class="tile-card" style="left:442px;top:2256px;width:318px;height:326px">
  <h4>Is it a boat? Is it a whale?... It's a Driftnest!</h4>
  <p>Easily one of the coolest inventions we've ever come across, the Driftnest is a versatile toy the whole family can enjoy together. Spend the day cruising along Seven Mile Beach in style as you bar hop with your clan. Better still, bring a cooler on board and put the kids to work paddling as you relax in your hammock on the crystal clear waters!</p>
</div>

<!-- column three -->
<div class="tile-photo" role="img" aria-label="Blue inflatable kayaks resting on white sand" style="left:763px;top:1358px;width:319px;height:213px;background:linear-gradient(180deg,#7fcfc6 0%,#c7e6dc 25%,#efe7d3 45%,#2f62b8 62%,#e6dcc4 78%,#d9cfb4 100%)"></div>
<div class="tile-card" style="left:763px;top:1571px;width:319px;height:200px">
  <h4>Enjoy complete freedom to explore.</h4>
  <p>Inflatable kayaks have revolutionized the way kayak exploration is done in a way never before. Our kayaks give you the freedom to explore Cayman's most secluded locations and snorkel those hard to reach reefs. Our kayaks are light, comfortable and easy to use.</p>
</div>
<div class="tile-photo" role="img" aria-label="Snorkelers in full face masks underwater" style="left:763px;top:1776px;width:319px;height:203px;background:linear-gradient(120deg,#4fb2d8 0%,#d97aa4 28%,#3c93c8 50%,#1f6ea8 100%)"></div>
<div class="tile-card" style="left:763px;top:1979px;width:319px;height:189px">
  <h4>There's no easier way to get around the island.</h4>
  <p>What better way is there to explore the island other than to rent a bike and go? Our mountain bikes are perfect for those interested on heading out on a full day adventure.</p>
</div>
<div class="tile-photo" role="img" aria-label="Sunken shipwreck in green blue water" style="left:763px;top:2168px;width:319px;height:194px;background:linear-gradient(180deg,#4aa0a0 0%,#3f8e88 40%,#2f6f74 70%,#1f5c6a 100%)"></div>
<div class="tile-card" style="left:763px;top:2362px;width:319px;height:220px">
  <h4>A new way to snorkel!</h4>
  <p>Our full face snorkel masks are easy to use, making them perfect for kids and beginners. You simply put the mask on and breath as you usually would. There's no need to get used to breathing from your mouth and you don't experience a sore jaw from having to hold the mouth piece in place. Just ask and we'll bring one along for you to try!</p>
</div>

<!-- top picks -->
<h2 class="picks-title abs">Our Adventure Top-Picks</h2>
<div class="pick abs" style="left:111px">
  <svg class="shape" width="250" height="158" viewBox="0 0 250 158" role="img" aria-label="Two people in a kayak on the water"><defs><linearGradient id="p1" x1="0" y1="0" x2="0" y2="1"><stop offset="0" stop-color="#8ccbe6"/><stop offset=".35" stop-color="#d9ecf2"/><stop offset=".6" stop-color="#4fb3d0"/><stop offset=".8" stop-color="#2f62b8"/><stop offset="1" stop-color="#2f8fb6"/></linearGradient></defs><path d="M6 14 C80 -4 160 24 244 8 C236 60 252 110 240 150 C160 136 90 162 10 148 C18 100 0 60 6 14Z" fill="url(#p1)"/></svg>
  <h5>Bio Bay</h5>
  <p>Lorem ipsum dolor sit amet conse ctetur adipiscing elit, sed do eiusmod tempor incididunt ut labore et dolore magna aliqua.</p>
  <a class="read-more" href="#">Read More</a>
</div>
<div class="pick abs" style="left:354px">
  <svg class="shape" width="250" height="158" viewBox="0 0 250 158" role="img" aria-label="Turquoise shallow sea with a distant shoreline"><defs><linearGradient id="p2" x1="0" y1="0" x2="0" y2="1"><stop offset="0" stop-color="#5f9fdc"/><stop offset=".3" stop-color="#a9d0ec"/><stop offset=".4" stop-color="#4f8f6a"/><stop offset=".5" stop-color="#5fd0cf"/><stop offset="1" stop-color="#35b3b6"/></linearGradient></defs><path d="M6 14 C80 -4 160 24 244 8 C236 60 252 110 240 150 C160 136 90 162 10 148 C18 100 0 60 6 14Z" fill="url(#p2)"/></svg>
  <h5>Kittiwake</h5>
  <p>Lorem ipsum dolor sit amet conse ctetur adipiscing elit, sed do eiusmod tempor incididunt ut labore et dolore magna aliqua.</p>
  <a class="read-more" href="#">Read More</a>
</div>
<div class="pick abs" style="left:595px">
  <svg class="shape" width="250" height="158" viewBox="0 0 250 158" role="img" aria-label="Bicycles parked by a beach"><defs><linearGradient id="p3" x1="0" y1="0" x2="0" y2="1"><stop offset="0" stop-color="#6faee0"/><stop offset=".35" stop-color="#bfe0ee"/><stop offset=".55" stop-color="#b8705a"/><stop offset=".75" stop-color="#d9c7a4"/><stop offset="1" stop-color="#c9b79a"/></linearGradient></defs><path d="M6 14 C80 -4 160 24 244 8 C236 60 252 110 240 150 C160 136 90 162 10 148 C18 100 0 60 6 14Z" fill="url(#p3)"/></svg>
  <h5>Sand Cay Island</h5>
  <p>Lorem ipsum dolor sit amet conse ctetur adipiscing elit, sed do eiusmod tempor incididunt ut labore et dolore magna aliqua.</p>
  <a class="read-more" href="#">Read More</a>
</div>
<div class="pick abs" style="left:838px">
  <svg class="shape" width="250" height="158" viewBox="0 0 250 158" role="img" aria-label="Person relaxing in a hammock boat on the water"><defs><linearGradient id="p4" x1="0" y1="0" x2="0" y2="1"><stop offset="0" stop-color="#6fc2b8"/><stop offset=".4" stop-color="#9fcf5a"/><stop offset=".6" stop-color="#4fb8b0"/><stop offset="1" stop-color="#2e8fa6"/></linearGradient></defs><path d="M6 14 C80 -4 160 24 244 8 C236 60 252 110 240 150 C160 136 90 162 10 148 C18 100 0 60 6 14Z" fill="url(#p4)"/></svg>
  <h5>Stingray City</h5>
  <p>Lorem ipsum dolor sit amet conse ctetur adipiscing elit, sed do eiusmod tempor incididunt ut labore et dolore magna aliqua.</p>
  <a class="read-more" href="#">Read More</a>
</div>

<!-- footer -->
<footer class="site-footer abs" role="img" aria-label="Deep blue underwater shipwreck scene"></footer>
<ul class="footer-col abs" style="left:165px">
  <li>Home</li><li>Adventures</li><li>Boats &amp; Rates</li><li>Captain's Blog</li><li>Gallery</li><li>Booking Enquiry</li><li>Contact</li>
</ul>
<ul class="footer-col abs" style="left:402px">
  <li>Palmreach Villas</li><li>Skylark Air</li><li>Reefline Kayaks</li><li>Kitewind Surf</li><li>Snorkeling Adventures!</li><li>Peripherals</li>
</ul>
<div class="footer-contact abs">
  <div>Tel: +1 (345) 555 0147</div>
  <div>fun@marlettoboats.com</div>
  <div class="gap"></div>
  <div class="footer-address">Marletto Boats Ltd<br>24 Harbour Lane<br>Seaview Park, George Town<br>Grand Cayman<br>Box 410 KY1-1420<br>Cayman Islands</div>
</div>
<div class="partner-badge abs" aria-hidden="true"></div>
<div class="bottom-bar abs">© 2017 marlettoboats.com</div>

</body>
</html>
```